Wholistic Health Clinic (Chiropractic Osteopathic Naturapathic Homeopathic New Website Design

Create a beautiful website for Fenwick Chiropractic clinic that has been in the Sutherland Shire for over 40 years, that exemplifies the passion for helping people with their health goals using that may include a variety of techniques including Chiropractic, Osteopathy, Acupuncture, Applied Kinesiology, Retained Neonatal Reflexes, Nutritional Advice, Exercise Prescription, Decompression therapy, Massage and Stress management techniques.
We have a wholistic approach that includes Nutritional, Emotional and Physical health

(A more detailed draft will be supplied shortly)

Pages:
Home page
About Us Page
Team Page
Contact page
Terms of service Page
Privacy Page
and any other relevant page(s)

Will supply photos for:
- The Team Page and their qualifications & brief resume
- About Us page

Will supply logos for:
BPN
TORVEX
PLORIVEN
GRANTLEAF
MVA
KPO

Target Market(s)

main target Parents of young children and those 20's to 60's who live in the Sutherland Shire & have disposable income (that said almost everybody would benefit from their services)

Coding

Coded - Design and coding required

Number of Pages Required

5+ page

Font styles to use
Sans Serif

Requirements
Must have
• Please follow the brief

1. Easy to manage ourselves to add alerts (like Covid 19 compliance & Harbel week etc.) & update content like photos of team members etc.
2. Must be responsive and look good on mobile devices
3. must be fast loading
4. Logo on every page
5. Easy navigation on every page
6. Phone number must be clickable
7. Terms of service & Privacy pages
8. Slider on page 1 using photo of healthy people of all ages enjoying various lifestyles & ability to add other photos easily
Should not have
• no testimonials or any non compliant elements according to the BPN

```html
<!DOCTYPE html>
<html lang="en">
<head>
<meta charset="utf-8">
<title>Fenwick Chiropractic Clinic</title>
<link href="https://fonts.googleapis.com/css2?family=Libre+Baskerville:wght@400;700&family=Open+Sans:wght@400;600;700&display=swap" rel="stylesheet">
<style>
:root{
  --blue:#2f5597;
  --blue-dark:#24467f;
  --green:#2e9e4f;
  --ink:#1f1f1f;
  --text:#6b6b6b;
  --light:#f4f4f4;
  --footer:#191919;
  --white:#ffffff;
}
*{margin:0;padding:0;box-sizing:border-box}
html,body{width:1200px;height:2432px;overflow:hidden;background:var(--white)}
body{font-family:"Open Sans",sans-serif;color:var(--ink);position:relative}
.serif{font-family:"Libre Baskerville",serif}

/* header */
.site-header{position:absolute;top:0;left:0;width:1200px;height:88px;display:flex;align-items:center;justify-content:space-between;padding:0 160px}
.brand{font-size:24px;font-weight:700;color:var(--ink)}
.main-nav{display:flex;align-items:center;gap:10px;font-size:14px}
.main-nav a{color:#333;text-decoration:none;padding:8px 14px}
.main-nav a.active{background:var(--blue);color:var(--white)}

/* hero */
.hero{position:absolute;top:88px;left:0;width:1200px;height:452px;background:linear-gradient(100deg,#6d5a4c 0%,#b89e86 40%,#e7d8c8 70%,#c8b6a3 100%);overflow:hidden}
.hero-title{position:absolute;left:160px;top:70px;color:var(--white);font-size:118px;line-height:1}
.hero-sub{position:absolute;left:160px;top:196px;color:var(--white);font-size:34px}
.hero-text{position:absolute;left:160px;top:252px;width:420px;color:var(--white);font-size:15px;line-height:1.5}
.btn-green{position:absolute;left:160px;top:320px;background:var(--green);color:var(--white);font-size:12px;font-weight:700;padding:10px 22px;letter-spacing:.5px}
.hero-arrow{position:absolute;top:208px}
.dots{position:absolute;left:576px;top:420px;display:flex;gap:10px}
.dots span{width:10px;height:10px;border-radius:50%;background:rgba(255,255,255,.6)}
.dots span.on{background:var(--white)}

/* about */
.about-frame{position:absolute;left:148px;top:614px;width:432px;height:268px;background:var(--blue)}
.about-photo{position:absolute;left:164px;top:626px;width:416px;height:262px;background:linear-gradient(135deg,#e9ddd2,#c9ad97 60%,#9c7f6b)}
.about-body{position:absolute;left:610px;top:640px;width:440px}
.section-title{color:var(--blue);font-size:38px}
.about-body p{margin-top:18px;font-size:14px;line-height:1.65;color:var(--text)}
.read-more{display:inline-block;margin-top:14px;font-size:12px;color:var(--blue);font-weight:600}

/* services */
.services-title{position:absolute;top:962px;left:0;width:1200px;text-align:center}
.card{position:absolute;top:1052px;width:424px;height:430px;background:var(--white);box-shadow:0 2px 10px rgba(0,0,0,.12);text-align:center}
.card-photo{height:270px}
.card h3{margin-top:22px;font-size:20px}
.card p{margin:12px 30px 0;font-size:13px;line-height:1.6;color:var(--text)}
.card .read-more{margin-top:10px}
.svc-arrow{position:absolute;top:1254px}
.btn-blue{position:absolute;left:538px;top:1496px;width:124px;height:36px;background:var(--blue);color:var(--white);font-size:12px;font-weight:700;display:flex;align-items:center;justify-content:center}

/* schedule */
.schedule{position:absolute;top:1572px;left:0;width:1200px;height:220px;background:linear-gradient(90deg,#2a2a2a,#4a4440 50%,#2e2b29)}
.schedule h2{position:absolute;left:232px;top:86px;color:var(--white);font-size:36px}
.btn-outline{position:absolute;left:772px;top:92px;width:208px;height:40px;border:1px solid var(--white);color:var(--white);font-size:12px;font-weight:600;display:flex;align-items:center;justify-content:center}

/* map */
.map{position:absolute;top:1792px;left:0;width:1200px;height:388px;background:linear-gradient(135deg,#e8eaec,#d9e6dc 45%,#cfdcea)}
.map-pin{position:absolute;left:574px;top:1960px}

/* footer */
.site-footer{position:absolute;top:2180px;left:0;width:1200px;height:252px;background:var(--footer);color:var(--white)}
.footer-brand{position:absolute;left:160px;top:34px;font-size:22px;font-weight:700;line-height:1.25}
.footer-col{position:absolute;top:36px}
.footer-col h4{font-family:"Libre Baskerville",serif;font-weight:400;font-size:18px;margin-bottom:18px}
.footer-col li{list-style:none;font-size:13px;color:#d0d0d0;margin-bottom:12px;display:flex;align-items:flex-start;gap:10px}
.copyright{position:absolute;left:0;bottom:14px;width:1200px;text-align:center;font-size:11px;color:#aaa;border-top:1px solid #333;padding-top:14px}
</style>
</head>
<body>

<header class="site-header">
  <div class="brand">Fenwick Chiropractic clinic</div>
  <nav class="main-nav">
    <a class="active">Home</a>
    <a>About Us</a>
    <a>Our Services</a>
    <a>Contact</a>
    <svg width="16" height="16" viewBox="0 0 16 16"><circle cx="6.5" cy="6.5" r="5" fill="none" stroke="#333" stroke-width="2"/><line x1="10.5" y1="10.5" x2="15" y2="15" stroke="#333" stroke-width="2"/></svg>
  </nav>
</header>

<section class="hero" role="img" aria-label="Chiropractor treating a smiling patient's shoulder">
  <div class="hero-title serif">Fenwick</div>
  <div class="hero-sub serif">Chiropractic Clinic</div>
  <p class="hero-text">Caring for the health of local families for over forty years, naturally.</p>
  <div class="btn-green">MAKE AN APPOINTMENT</div>
  <svg class="hero-arrow" style="left:30px" width="26" height="26" viewBox="0 0 26 26"><path d="M20 13H6M12 6l-7 7 7 7" fill="none" stroke="#fff" stroke-width="3"/></svg>
  <svg class="hero-arrow" style="right:30px" width="26" height="26" viewBox="0 0 26 26"><path d="M6 13h14M14 6l7 7-7 7" fill="none" stroke="#fff" stroke-width="3"/></svg>
  <div class="dots"><span class="on"></span><span></span><span></span></div>
</section>

<div class="about-frame"></div>
<div class="about-photo" role="img" aria-label="Patient lying face down receiving a back treatment"></div>
<section class="about-body">
  <h2 class="section-title serif">About Us</h2>
  <p>For more than forty years our clinic has helped families across the Sutherland Shire move, sleep and feel better. We look at the whole person, blending chiropractic care with nutrition, exercise and stress management so every plan fits your life. From newborns to grandparents, our gentle team listens first, explains clearly and works with you toward lasting health goals you can keep.</p>
  <span class="read-more">READ MORE »</span>
</section>

<h2 class="services-title section-title serif">Our Services</h2>
<svg class="svc-arrow" style="left:76px" width="26" height="22" viewBox="0 0 26 22"><path d="M24 11H3M11 3l-8 8 8 8" fill="none" stroke="#222" stroke-width="2.5"/></svg>
<svg class="svc-arrow" style="left:1098px" width="26" height="22" viewBox="0 0 26 22"><path d="M2 11h21M15 3l8 8-8 8" fill="none" stroke="#222" stroke-width="2.5"/></svg>

<article class="card" style="left:164px">
  <div class="card-photo" role="img" aria-label="Therapist adjusting a patient's upper back" style="background:linear-gradient(135deg,#d8c3b2,#a88b76 55%,#7d6352)"></div>
  <h3 class="serif">Chiropractic Therapy</h3>
  <p>Gentle spinal adjustments that ease pain, restore movement and help your body work the way it should, at every age.</p>
  <span class="read-more">READ MORE »</span>
</article>
<article class="card" style="left:612px">
  <div class="card-photo" role="img" aria-label="Therapist stretching a patient's arm and shoulder" style="background:linear-gradient(135deg,#eeeae6,#cdbfb3 55%,#9d8a7c)"></div>
  <h3 class="serif">Osteopathy Therapy</h3>
  <p>Hands-on treatment of muscles, joints and posture to relieve tension and support recovery after injury or strain.</p>
  <span class="read-more">READ MORE »</span>
</article>

<div class="btn-blue">VIEW ALL</div>

<section class="schedule" role="img" aria-label="Dim photo of a back massage in the clinic">
  <h2 class="serif">Schedule An Appointment</h2>
  <div class="btn-outline">SCHEDULE NOW</div>
</section>

<div class="map" role="img" aria-label="Street map showing the clinic location"></div>
<svg class="map-pin" width="28" height="38" viewBox="0 0 28 38"><path d="M14 1C7 1 1 6.5 1 13.5 1 23 14 37 14 37s13-14 13-23.5C27 6.5 21 1 14 1z" fill="#d93025"/><circle cx="14" cy="13.5" r="5" fill="#8e1b14"/></svg>

<footer class="site-footer">
  <div class="footer-brand">Fenwick<br>Chiropractic clinic</div>
  <div class="footer-col" style="left:388px">
    <h4>Site Map</h4>
    <ul><li>Home</li><li>About Us</li><li>Our Services</li><li>Contact</li></ul>
  </div>
  <div class="footer-col" style="left:612px">
    <h4>Quick Links</h4>
    <ul><li>Privacy Policy</li><li>Terms &amp; Conditions</li><li>FAQs</li><li>Blogs</li></ul>
  </div>
  <div class="footer-col" style="left:836px">
    <h4>Contact Us</h4>
    <ul>
      <li><svg width="14" height="14" viewBox="0 0 14 14"><path d="M3 1l2.5 3-1.5 1.5c.8 1.8 2.2 3.2 4 4L9.5 8l3 2.5-1.5 2.5C6 13 1 8 1 2.5z" fill="#fff"/></svg>+61 2 5550 1842</li>
      <li><svg width="14" height="14" viewBox="0 0 14 14"><rect x="1" y="3" width="12" height="8" fill="none" stroke="#fff" stroke-width="1.4"/><path d="M1 3l6 5 6-5" fill="none" stroke="#fff" stroke-width="1.4"/></svg>hello@fenwickclinic.au</li>
      <li><svg width="14" height="14" viewBox="0 0 14 18"><path d="M7 1C3.7 1 1 3.6 1 6.8 1 11.3 7 17 7 17s6-5.7 6-10.2C13 3.6 10.3 1 7 1z" fill="#fff"/><circle cx="7" cy="6.8" r="2.2" fill="#191919"/></svg>52 Ash Avenue,<br>Kirrawee NSW 2232</li>
    </ul>
  </div>
  <div class="copyright">2024 Copyright © Fenwick Chiropractic Clinic &nbsp;|&nbsp; All Rights Reserved</div>
</footer>

</body>
</html>
```